Security based company delivering High Risk Training to Law Enforcement Agencies Worldwide.

We need a Web design for a company doing business in Washington D.C. We deliver High Risk Training to Law Enforcement Agencies throughout the world. Our focus is on Improvised Explosive Devices. We train Bomb Technicians and First Responders in all aspects relating to bombings and criminal incidents globally.

Reason: We have uploaded our logo. Thank you.

Target Market(s)

Military and Law Enforcement Personnel from around the world.

Industry/Entity Type

Business

Requirements
Should not have
• Do not include cartoon like characters.

```html
<!DOCTYPE html>
<html lang="en">
<head>
<meta charset="utf-8">
<title>Halvorn International</title>
<link href="https://fonts.googleapis.com/css2?family=Arimo:wght@400;700&display=swap" rel="stylesheet">
<style>
:root{
  --navy:#13237e;
  --navy-deep:#0c1a6e;
  --red:#d6121b;
  --ink:#333333;
  --muted:#8b8b8b;
  --rule:#e3e3e3;
  --panel:#ececec;
  --white:#ffffff;
}
*{box-sizing:border-box;margin:0;padding:0}
html,body{width:995px;height:1200px;overflow:hidden;background:var(--white)}
body{position:relative;font-family:"Arimo",Arial,sans-serif;color:var(--ink)}
.abs{position:absolute}

.top-bar{left:0;top:0;width:995px;height:5px;background:#7a7a7a}

/* header */
.brand{left:121px;top:40px;display:flex;align-items:center;gap:12px}
.brand-mark{width:44px;height:44px;background:var(--navy)}
.brand-name{font-weight:700;font-size:26px;color:var(--ink);letter-spacing:.5px;line-height:1}
.brand-sub{display:block;font-size:12px;letter-spacing:1px;margin-top:4px;color:var(--ink)}
.account{right:114px;top:25px;display:flex;align-items:center;gap:10px;font-size:12px}
.login{background:var(--red);color:var(--white);border-radius:10px;padding:3px 14px}
.signup{color:var(--ink)}
.nav{left:539px;top:68px;width:341px;display:flex;justify-content:space-between;font-size:11.5px;text-transform:uppercase;white-space:nowrap}
.nav a{color:var(--ink);text-decoration:none}
.nav a.active{color:var(--red)}
.nav-rule{left:539px;top:88px;width:341px;height:4px;background:#7a7a7a}
.nav-rule-active{left:539px;top:88px;width:39px;height:4px;background:var(--red)}

/* hero */
.hero-band{left:0;top:117px;width:995px;height:377px;background:linear-gradient(180deg,#b9a48a,#d9cbb8 55%,#cdbda6)}
.slider{left:115px;top:141px;width:765px;height:330px;background:var(--white);padding:6px}
.slide-photo{width:100%;height:100%;background:linear-gradient(100deg,#c2b29c 0%,#b8a68e 35%,#8f8274 60%,#b5a38b 80%,#c7b6a0 100%)}
.caption{left:121px;top:396px;width:753px;height:69px;background:rgba(40,40,40,.82);color:var(--white);font-size:12px;line-height:16px;padding:23px 11px 0;text-transform:uppercase}
.arrow{top:276px;width:22px;height:28px;background:var(--white)}
.arrow-prev{left:121px}
.arrow-next{left:852px}
.dot{left:855px;width:9px;height:9px;border-radius:50%;background:#e8e8e8}
.dot.on{background:var(--red)}

/* headings */
.section-title{font-size:16px;color:var(--navy);text-transform:uppercase;font-weight:400}
.section-title em{font-style:normal;color:var(--red)}
.rule{height:5px;background:var(--rule)}

.intro{left:115px;top:564px;width:496px;font-size:10.3px;line-height:14.5px;text-align:justify;color:#444}
.intro p+p{margin-top:14px}

.courses{left:634px;top:565px;width:246px;list-style:none;font-size:11px;text-transform:uppercase;color:#444}
.courses li{height:23px;display:flex;align-items:center;gap:12px}
.courses li::before{content:"";width:11px;height:11px;border-radius:50%;background:var(--muted)}
.view-all{left:657px;top:707px;font-size:11px;color:var(--red);text-transform:uppercase}

/* cards */
.card{width:235px;height:95px}
.card-photo{position:absolute;left:0;top:0;width:99px;height:93px;border:1px solid #ddd;padding:4px;background:var(--white)}
.card-photo div{width:100%;height:100%;background:linear-gradient(135deg,#c9c9c2,#5b6548 55%,#8d9478)}
.card-title{position:absolute;left:106px;top:0;width:130px;font-size:10.5px;line-height:16px;font-weight:700;color:var(--navy);text-transform:uppercase;white-space:nowrap}
.card-text{position:absolute;left:106px;top:38px;width:129px;font-size:10.3px;line-height:14.5px;text-align:justify;color:#444}
.card-text b{color:var(--red)}

/* categories */
.categories{left:634px;top:774px;width:246px;height:249px;background:var(--panel)}
.cat-head{height:33px;background:var(--navy);color:var(--white);font-size:16px;padding:8px 11px;text-transform:uppercase}
.cat-intro{font-size:10.3px;line-height:15px;text-align:center;padding:6px 8px 8px;color:#444}
.cat-list{list-style:none;font-size:10px;font-weight:700;color:#444}
.cat-list li{height:21.4px;border-top:1px solid #fafafa;display:flex;align-items:center;padding-left:11px;gap:9px}
.cat-list li::before{content:"›";font-size:14px;line-height:1;margin-top:-2px}
.cat-list li.more{color:var(--red)}

/* footer */
.footer-red{left:0;top:1081px;width:995px;height:6px;background:var(--red)}
.footer{left:0;top:1087px;width:995px;height:113px;background:linear-gradient(180deg,var(--navy-deep),#122a86)}
.foot-nav{left:115px;top:1122px;font-size:10px;color:var(--white);display:flex;gap:14px}
.foot-nav span.sep{opacity:.8}
.join{left:740px;top:1122px;font-size:10px;color:var(--white)}
.social{top:1114px;width:26px;height:26px;border-radius:50%}
.foot-line{left:115px;top:1167px;width:765px;height:1px;background:#2d43a0}
.copyright{left:117px;top:1179px;font-size:9.5px;color:#c7cbe6}
</style>
</head>
<body>
<div class="abs top-bar"></div>

<header>
  <div class="abs brand">
    <div class="brand-mark"></div>
    <div class="brand-name">HALVORN<span class="brand-sub">INTERNATIONAL</span></div>
  </div>
  <div class="abs account"><span class="login">LOGIN</span><span>/</span><span class="signup">SIGN UP</span></div>
  <nav class="abs nav">
    <a class="active" href="#">Home</a><a href="#">About Us</a><a href="#">Services</a><a href="#">Testimonials</a><a href="#">Contact Us</a>
  </nav>
  <div class="abs nav-rule"></div>
  <div class="abs nav-rule-active"></div>
</header>

<section>
  <div class="abs hero-band" role="img" aria-label="Blurred desert training ground"></div>
  <div class="abs slider"><div class="slide-photo" role="img" aria-label="Photo of a controlled detonation on a desert training range"></div></div>
  <div class="abs caption">Lorem ipsum dolor sit amet, consectetuer adipiscing elit, sed diam nonummy nibh euismod tincidunt ut laoreet dolore magna aliquam erat volutpat.</div>
  <svg class="abs arrow arrow-prev" viewBox="0 0 22 28"><path d="M14 6 L7 14 L14 22" fill="none" stroke="#d6121b" stroke-width="2"/></svg>
  <svg class="abs arrow arrow-next" viewBox="0 0 22 28"><path d="M8 6 L15 14 L8 22" fill="none" stroke="#222" stroke-width="2"/></svg>
  <div class="abs dot" style="top:162px"></div>
  <div class="abs dot on" style="top:175px"></div>
  <div class="abs dot" style="top:188px"></div>
</section>

<main>
  <h2 class="abs section-title" style="left:115px;top:522px">Welcome to <em>Halvorn International</em></h2>
  <div class="abs rule" style="left:115px;top:544px;width:496px"></div>
  <div class="abs intro">
    <p>Lorem ipsum dolor sit amet, consectetuer adipiscing elit, sed diam nonummy nibh euismod tincidunt ut laoreet dolore magna aliquam erat volutpat. Ut wisi enim ad minim veniam, quis nostrud exerci tation ullamcorper suscipit lobortis nisl ut aliquip ex ea commodo consequat. Duis autem vel eum iriure dolor in hendrerit in vulputate velit esse molestie consequat, vel illum dolore eu feugiat nulla facilisis at vero eros et accumsan et iusto odio dignissim qui blandit praesent luptatum zzril delenit augue duis dolore te feugait nulla facilisi.</p>
    <p>Ut wisi enim ad minim veniam, quis nostrud exerci tation ullamcorper suscipit lobortis nisl ut aliquip ex ea commodo consequat. Duis autem vel eum iriure dolor in hendrerit in vulputate velit esse molestie consequat, vel illum dolore eu feugiat nulla facilisis at vero eros et accumsan et iusto odio dignissim qui blandit praesent luptatum zzril delenit augue duis dolore te feugait nulla facilisi. Lorem ipsum dolor sit amet, consectetuer adipiscing elit, sed diam nonummy nibh euismod tincidunt ut laoreet dolore magna aliquam erat volutpat.</p>
  </div>

  <h2 class="abs section-title" style="left:634px;top:522px">Courses <em>Offered</em></h2>
  <div class="abs rule" style="left:634px;top:544px;width:246px"></div>
  <ul class="abs courses">
    <li>Consectetuer adipiscing elit</li>
    <li>Lorem ipsum dolor sit</li>
    <li>Ullamcorper suscipit</li>
    <li>Hendrerit in vulputate velit</li>
    <li>Ullamcorper suscipit</li>
    <li>Adipiscing elit</li>
  </ul>
  <div class="abs view-all">View All</div>

  <h2 class="abs section-title" style="left:115px;top:771px">Lorem ipsum <em>consectetuer adipiscing</em></h2>
  <div class="abs rule" style="left:115px;top:794px;width:496px"></div>

  <article class="abs card" style="left:115px;top:810px">
    <div class="card-photo"><div role="img" aria-label="Technician in a bomb disposal suit"></div></div>
    <h3 class="card-title">Consectetuer elit<br>lorem ipsum dolor</h3>
    <p class="card-text">Lorem ipsum dolor sit amet, consectetuer adipiscing elit, sed diam nonummy nibh euismod. <b>Read</b></p>
  </article>
  <article class="abs card" style="left:376px;top:810px">
    <div class="card-photo"><div role="img" aria-label="Technician in a bomb disposal suit"></div></div>
    <h3 class="card-title">Consectetuer elit<br>lorem ipsum dolor</h3>
    <p class="card-text">Lorem ipsum dolor sit amet, consectetuer adipiscing elit, sed diam nonummy nibh euismod. <b>Read</b></p>
  </article>
  <article class="abs card" style="left:115px;top:932px">
    <div class="card-photo"><div role="img" aria-label="Technician in a bomb disposal suit"></div></div>
    <h3 class="card-title">Consectetuer elit<br>lorem ipsum dolor</h3>
    <p class="card-text">Lorem ipsum dolor sit amet, consectetuer adipiscing elit, sed diam nonummy nibh euismod. <b>Read</b></p>
  </article>
  <article class="abs card" style="left:376px;top:932px">
    <div class="card-photo"><div role="img" aria-label="Technician in a bomb disposal suit"></div></div>
    <h3 class="card-title">Consectetuer elit<br>lorem ipsum dolor</h3>
    <p class="card-text">Lorem ipsum dolor sit amet, consectetuer adipiscing elit, sed diam nonummy nibh euismod. <b>Read</b></p>
  </article>

  <aside class="abs categories">
    <div class="cat-head">Categories</div>
    <p class="cat-intro">Lorem ipsum dolor sit amet, consectetuer adipiscing elit, sed diam nonummy nibh euismod dolore te feugait nulla facilisi.</p>
    <ul class="cat-list">
      <li>Lorem ipsum dolor</li>
      <li>Consectetuer adipiscing elit</li>
      <li>Quis nostrud exerci tation</li>
      <li>Vulputate velit esse</li>
      <li>Hendrerit in vulputate velit</li>
      <li>Ullamcorper Suscipit</li>
      <li class="more">View All</li>
    </ul>
  </aside>
</main>

<footer>
  <div class="abs footer-red"></div>
  <div class="abs footer"></div>
  <nav class="abs foot-nav">
    <span>Home</span><span class="sep">|</span><span>About Us</span><span class="sep">|</span><span>Services</span><span class="sep">|</span><span>Testimonials</span><span class="sep">|</span><span>Contact Us</span>
  </nav>
  <div class="abs join">Join Us:</div>
  <div class="abs social" style="left:783px;background:#3b5aa8" aria-label="Social link"></div>
  <div class="abs social" style="left:815px;background:#3d8fd6" aria-label="Social link"></div>
  <div class="abs social" style="left:847px;background:#d8452f" aria-label="Social link"></div>
  <div class="abs foot-line"></div>
  <div class="abs copyright">© 2014 Halvorn International. All Rights Reserved.</div>
</footer>
</body>
</html>
```